Initial website for sport tech startup

We are currently in the R&D phases of our new product. It’s a headband to prevent concussion in the soccer market initially.

We have 2 products, one that’s basic aimed at the youth market and the other more technology driven that’s aimed at the academies and professional market.

Initially the product will launch in the UK

Target Market(s)

Youth soccer players and parents in UK, Soccer Clubs, Federations.

Industry/Entity Type

Sporting Good

Coding

Coded - Design and coding required

Number of Pages Required

5+ page

Requirements
Must have
• Professional style that can be adapted and changed over the coming months.
Nice to have
• Ecommerce ability in the future.

```html
<!DOCTYPE html>
<html lang="en">
<head>
<meta charset="utf-8">
<title>Guardline – Making Sport Safer</title>
<link href="https://fonts.googleapis.com/css2?family=Montserrat:wght@500;700;800&family=Roboto:wght@300;400;500;700&display=swap" rel="stylesheet">
<style>
:root{
  --blue:#1d7ae6;
  --navy:#0f4c8a;
  --ink:#1e2430;
  --text:#4b5260;
  --muted:#a3a8b2;
  --topbar:#4a5260;
  --band:#2b3242;
  --footer:#262c3a;
  --footer-bottom:#1f2430;
  --hero:#f3f3f4;
  --line:#e6e8ec;
  --pale-btn:#dfe5ec;
}
*{box-sizing:border-box;margin:0;padding:0}
html,body{width:1200px;height:3165px;overflow:hidden}
body{position:relative;background:#fff;font-family:"Roboto",sans-serif;color:var(--text)}
.abs{position:absolute}
.center{left:0;width:1200px;text-align:center}
.topbar{left:0;top:0;width:1200px;height:32px;background:var(--topbar);color:#e4e7ec;font-size:10px}
.topbar span{position:absolute;top:10px}
.dot{display:inline-block;width:9px;height:9px;border-radius:50%;background:#c9ced6;position:absolute;top:11px}
.hero{left:0;top:32px;width:1200px;height:498px;background:var(--hero)}
.logo{left:235px;top:49px;width:127px;height:32px;font:500 22px/32px "Roboto",sans-serif;color:var(--navy);letter-spacing:1px}
.nav{top:55px;font:500 11px/14px "Roboto",sans-serif;color:var(--ink)}
.nav-active{border-bottom:2px solid var(--blue);padding-bottom:6px}
.hero-title{top:128px;font:800 31px/36px "Montserrat",sans-serif;color:#111;letter-spacing:.5px}
.hero-sub{top:170px;font:400 14px/20px "Roboto",sans-serif;color:#222}
.product-art{left:344px;top:215px;width:509px;height:255px;border-radius:40px 40px 0 0;background:linear-gradient(160deg,#5b616c,#3a404b)}
.call{left:683px;top:390px;width:151px;height:34px;border-radius:17px;background:var(--navy);color:#fff}
.call small{position:absolute;left:44px;top:6px;font-size:8px;color:#bcd4ee}
.call b{position:absolute;left:44px;top:16px;font:400 12px/14px "Roboto",sans-serif}
.features{left:235px;top:470px;width:729px;height:224px;background:#fff;box-shadow:0 8px 24px rgba(0,0,0,.12)}
.feature{position:absolute;top:0;width:243px;height:224px;text-align:center}
.feature+.feature{border-left:1px solid var(--line)}
.feature svg{margin-top:22px}
.feature h3{font:500 15px/18px "Roboto",sans-serif;color:var(--ink);margin-top:10px}
.feature p{font-size:11px;line-height:16px;margin:14px auto 0;width:170px}
.btn{display:inline-block;width:102px;height:27px;border-radius:14px;font:500 9px/27px "Roboto",sans-serif;background:var(--pale-btn);color:var(--ink);margin-top:24px}
.btn-primary{background:var(--navy);color:#fff;box-shadow:0 4px 10px rgba(15,76,138,.35)}
.section-title{font:400 22px/26px "Roboto",sans-serif;color:var(--ink)}
.underline{left:578px;width:44px;height:3px;background:var(--blue)}
.photo{background:linear-gradient(135deg,#3e4a55,#8b9299 55%,#3d6b3a)}
.about-head{left:642px;top:819px;width:330px;font:700 13px/22px "Roboto",sans-serif;color:var(--ink)}
.about-text{left:642px;width:320px;font-size:12px;line-height:20px;color:#333}
.band{left:0;top:1099px;width:1200px;height:173px;background:var(--band);color:#fff}
.band-item{position:absolute;top:64px;font:500 10px/15px "Roboto",sans-serif;letter-spacing:.2px}
.card{background:#fff;border:1px solid var(--line)}
.card h4{position:absolute;font:500 11px/14px "Roboto",sans-serif;color:var(--ink)}
.meta{position:absolute;font-size:7px;color:#555}
.meta em{font-style:normal;color:var(--blue)}
.card p{position:absolute;font-size:10px;line-height:15px;color:#666}
.more{position:absolute;font-size:7px;color:var(--muted);text-decoration:underline}
.date{position:absolute;left:0;width:88px;text-align:center}
.date b{display:block;font:700 28px/30px "Montserrat",sans-serif;color:var(--blue)}
.date span{display:block;font:700 8px/12px "Roboto",sans-serif;letter-spacing:2px;color:var(--blue);margin-top:4px}
.avatar{border-radius:50%;background:linear-gradient(180deg,#d9d5d0,#8c8f96)}
.member{position:absolute;top:1942px;width:160px;text-align:center}
.member b{display:block;font:500 11px/14px "Roboto",sans-serif;color:var(--ink)}
.member span{display:block;font-size:9px;color:var(--muted);margin-top:4px}
.gallery{left:0;top:2020px;width:1200px;height:394px;background:var(--band)}
.tile{background:#b7b9bd}
.quote{position:absolute;top:2533px;width:260px}
.quote-title{font:500 12px/16px "Roboto",sans-serif;color:var(--blue)}
.quote-title span{font-size:16px;line-height:16px;margin-right:8px}
.quote-text{font-size:11.5px;line-height:19px;color:#333;margin-top:8px}
.quote-name{font:700 10px/14px "Roboto",sans-serif;color:var(--ink);margin-top:6px}
.quote-role{font-size:8px;line-height:12px;color:var(--muted);margin-top:2px}
.footer{left:0;top:2929px;width:1200px;height:236px;background:var(--footer);color:#c9ced6}
.footer-bottom{left:0;top:3133px;width:1200px;height:32px;background:var(--footer-bottom);color:#717887;font-size:8px}
.fcol{position:absolute;top:53px;font-size:9px}
.fcol h5{font:500 8px/12px "Roboto",sans-serif;color:#fff;letter-spacing:.3px;margin-bottom:13px}
.fcol li{list-style:none;line-height:22.5px}
.social{position:absolute;top:140px;width:22px;height:22px;border-radius:50%;border:1px solid #4a5263}
</style>
</head>
<body>

<div class="abs topbar">
  <span style="left:235px">&#9742; 1 (000) 000-0000</span>
  <span style="left:340px">&#9993; hello@guardline.example</span>
  <i class="dot" style="left:916px"></i><i class="dot" style="left:936px"></i><i class="dot" style="left:956px"></i>
</div>

<div class="abs hero"></div>
<div class="abs logo">GUARDLINE</div>
<div class="abs nav nav-active" style="left:604px">HOME</div>
<div class="abs nav" style="left:667px">ABOUT</div>
<div class="abs nav" style="left:730px">PRODUCTS</div>
<div class="abs nav" style="left:813px">SHOP</div>
<div class="abs nav" style="left:870px">CONTACT</div>
<svg class="abs" style="left:940px;top:49px" width="26" height="24" viewBox="0 0 26 24"><path d="M1 4h4l3 11h11l3-8H7" fill="none" stroke="#555" stroke-width="1.6"/><circle cx="10" cy="19" r="1.6" fill="#555"/><circle cx="18" cy="19" r="1.6" fill="#555"/><circle cx="19" cy="4" r="5" fill="var(--blue)"/></svg>

<div class="abs center hero-title">MAKING SPORT SAFER</div>
<div class="abs center hero-sub">GUARDLINE BRINGING SAFETY TO THE<br>SPORTS CONCUSSION DEBATE</div>
<div class="abs product-art" role="img" aria-label="Protective sports headband illustration"></div>
<div class="abs call">
  <svg class="abs" style="left:14px;top:8px" width="20" height="18" viewBox="0 0 20 18"><path d="M3 2c2-1 3 3 2 4s2 5 4 6 3-1 4 1-1 3-3 3C5 15 0 6 3 2z" fill="#f2b233"/></svg>
  <small>Call Us On</small><b>+44 20 0000 1234</b>
</div>

<div class="abs features">
  <div class="feature" style="left:0">
    <svg width="36" height="38" viewBox="0 0 36 38" fill="none" stroke="var(--navy)" stroke-width="1.5"><rect x="6" y="3" width="24" height="30" rx="2"/><path d="M11 10h14M11 15h14M11 20h8M9 30l4 4 8-10"/></svg>
    <h3>Safety Tested</h3><p>Lorem Ipsum is simply dummy text of the printing and</p><span class="btn">SHOP NOW</span>
  </div>
  <div class="feature" style="left:243px">
    <svg width="38" height="38" viewBox="0 0 38 38" fill="none" stroke="var(--navy)" stroke-width="1.5"><path d="M6 22c4-10 18-16 26-14-4 8-14 14-26 14z"/><path d="M8 28h24M12 32h16"/></svg>
    <h3>Light Weight</h3><p>Lorem Ipsum is simply dummy text of the printing and</p><span class="btn btn-primary">SHOP NOW</span>
  </div>
  <div class="feature" style="left:486px">
    <svg width="38" height="38" viewBox="0 0 38 38" fill="none" stroke="var(--navy)" stroke-width="1.5"><circle cx="22" cy="5" r="3"/><path d="M20 9l-6 10 6 5-4 10M14 19l-8 4M20 12l8 4"/><circle cx="30" cy="31" r="4"/></svg>
    <h3>Comfortable</h3><p>Lorem Ipsum is simply dummy text of the printing and</p><span class="btn">SHOP NOW</span>
  </div>
</div>

<div class="abs center section-title" style="top:742px">BRINGING SAFETY TO THE SPORTS</div>
<div class="abs underline" style="top:780px"></div>
<div class="abs photo" style="left:235px;top:815px;width:356px;height:235px;box-shadow:0 8px 18px rgba(0,0,0,.15)" role="img" aria-label="Goalkeeper diving to catch a football in a stadium"></div>
<div class="abs about-head">GUARDLINE – BRINGING SAFETY TO THE SPORTS CONCUSSION DEBATE</div>
<div class="abs about-text" style="top:878px">Guardline is designing and developing head protectio Guardline protection products to reduce the likelihood of concussion when playing sports.</div>
<div class="abs about-text" style="top:951px">Exploring and understanding medical insights, material science and composites research, current and former players experiences and governing bodies guidelines has allowed Guardline to develop the safety</div>

<div class="abs band">
  <svg class="abs" style="left:275px;top:56px" width="50" height="52" viewBox="0 0 50 52" fill="none" stroke="#fff" stroke-width="1.5"><circle cx="14" cy="6" r="4"/><path d="M14 12l-6 14 10 6-6 16M8 26l-6-4M18 20l12 6"/><circle cx="40" cy="34" r="6"/></svg>
  <div class="band-item" style="left:342px">FUNCTIONAL &amp;<br>PROTECTIVE HEADGEAR<br>THAT IS APPEALING</div>
  <svg class="abs" style="left:512px;top:58px" width="42" height="50" viewBox="0 0 42 50" fill="none" stroke="#fff" stroke-width="1.5"><rect x="2" y="2" width="32" height="44"/><circle cx="12" cy="12" r="5"/><path d="M20 10h10M20 16h10M8 26h22M8 32h22M8 38h14"/><circle cx="34" cy="40" r="6"/></svg>
  <div class="band-item" style="left:569px">ALLOWING FOR NEW<br>CATEGORIES OF DATA<br>CAPTURE AND ANALYTICS</div>
  <svg class="abs" style="left:733px;top:56px" width="52" height="52" viewBox="0 0 52 52" fill="none" stroke="#fff" stroke-width="1.5"><circle cx="26" cy="8" r="5"/><circle cx="8" cy="40" r="5"/><circle cx="44" cy="40" r="5"/><rect x="18" y="16" width="16" height="10"/><rect x="2" y="46" width="12" height="5"/><rect x="38" y="46" width="12" height="5"/><path d="M14 14a18 18 0 0 0-8 18M38 14a18 18 0 0 1 8 18M18 44h16"/></svg>
  <div class="band-item" style="left:802px;top:71px">WORKING GROUP TO<br>CARRY OUT INTIAL TRIALS</div>
</div>

<div class="abs center section-title" style="top:1319px">Events &amp; Blogs</div>
<div class="abs underline" style="top:1357px"></div>

<div class="abs card" style="left:235px;top:1391px;width:418px;height:137px">
  <div class="abs photo" style="left:0;top:0;width:186px;height:135px" role="img" aria-label="Goalkeeper catching a ball"></div>
  <h4 style="left:205px;top:20px">Lorem Ipsum is simply dummy text</h4>
  <div class="meta" style="left:205px;top:42px">POSTED 08.17.2017 | <em>BY LEE HART</em></div>
  <p style="left:205px;top:60px;width:200px">Lorem Ipsum is simply dummy text of the printing and typesetting industry</p>
  <div class="more" style="left:205px;top:100px">VIEW DETAILS</div>
</div>
<div class="abs card" style="left:235px;top:1541px;width:418px;height:136px">
  <div class="abs photo" style="left:0;top:0;width:186px;height:134px;background:linear-gradient(160deg,#c8ccd0,#7d2a32 45%,#3b7a35)" role="img" aria-label="Player's foot on a football on grass"></div>
  <h4 style="left:205px;top:20px">Lorem Ipsum is simply dummy text</h4>
  <div class="meta" style="left:205px;top:42px">POSTED 08.17.2017 | <em>BY LEE HART</em></div>
  <p style="left:205px;top:60px;width:200px">Lorem Ipsum is simply dummy text of the printing and typesetting industry</p>
  <div class="more" style="left:205px;top:100px">VIEW DETAILS</div>
</div>

<div class="abs card" style="left:672px;top:1391px;width:292px;height:87px">
  <div class="date" style="top:20px"><b>04</b><span>DEC</span></div>
  <h4 style="left:86px;top:20px">Lorem Ipsum is simply dummy</h4>
  <div class="meta" style="left:86px;top:42px">POSTED 08.17.2017 | <em>BY LEE HART</em></div>
  <div class="more" style="left:86px;top:62px">VIEW DETAILS</div>
</div>
<div class="abs card" style="left:672px;top:1491px;width:292px;height:87px">
  <div class="date" style="top:20px"><b>22</b><span>JUN</span></div>
  <h4 style="left:86px;top:20px">Lorem Ipsum is simply dummy</h4>
  <div class="meta" style="left:86px;top:42px">POSTED 08.17.2017 | <em>BY LEE HART</em></div>
  <div class="more" style="left:86px;top:62px">VIEW DETAILS</div>
</div>
<div class="abs card" style="left:672px;top:1589px;width:292px;height:87px">
  <div class="date" style="top:20px"><b>15</b><span>AUG</span></div>
  <h4 style="left:86px;top:20px">Lorem Ipsum is simply dummy</h4>
  <div class="meta" style="left:86px;top:42px">POSTED 08.17.2017 | <em>BY LEE HART</em></div>
  <div class="more" style="left:86px;top:62px">VIEW DETAILS</div>
</div>

<div class="abs center section-title" style="top:1724px">Our Team</div>
<div class="abs underline" style="top:1763px"></div>
<div class="abs avatar" style="left:255px;top:1801px;width:126px;height:126px" role="img" aria-label="Team member portrait"></div>
<div class="abs avatar" style="left:443px;top:1801px;width:126px;height:126px" role="img" aria-label="Team member portrait"></div>
<div class="abs avatar" style="left:631px;top:1801px;width:126px;height:126px" role="img" aria-label="Team member portrait"></div>
<div class="abs avatar" style="left:817px;top:1801px;width:126px;height:126px" role="img" aria-label="Team member portrait"></div>
<div class="member" style="left:238px"><b>Name</b><span>Lorem Ipsum is simply</span></div>
<div class="member" style="left:426px"><b>Name</b><span>Lorem Ipsum is simply</span></div>
<div class="member" style="left:614px"><b>Name</b><span>Lorem Ipsum is simply</span></div>
<div class="member" style="left:800px"><b>Name</b><span>Lorem Ipsum is simply</span></div>

<div class="abs gallery"></div>
<div class="abs section-title" style="left:232px;top:2054px;color:#fff">Product Gallery</div>
<div class="abs" style="left:234px;top:2094px;width:44px;height:3px;background:var(--blue)"></div>
<div class="abs" style="left:873px;top:2059px;width:91px;height:29px;border-radius:15px;background:var(--blue);color:#fff;font:500 8px/29px Roboto,sans-serif;text-align:center">VIEW ALL</div>
<div class="abs tile" style="left:233px;top:2127px;width:356px;height:249px;background:linear-gradient(180deg,#b8babe 55%,#3a4050)" role="img" aria-label="Protective headband product shot"></div>
<div class="abs tile" style="left:609px;top:2127px;width:168px;height:115px"></div>
<div class="abs tile" style="left:797px;top:2127px;width:168px;height:115px"></div>
<div class="abs tile" style="left:609px;top:2262px;width:168px;height:114px"></div>
<div class="abs tile" style="left:797px;top:2262px;width:168px;height:114px"></div>

<div class="abs center section-title" style="top:2460px">QUOTES</div>
<div class="abs underline" style="top:2498px"></div>

<div class="abs avatar" style="left:233px;top:2558px;width:86px;height:86px" role="img" aria-label="Customer portrait"></div>
<div class="quote" style="left:343px">
  <div class="quote-title"><span>&#8220;</span>Lorem Ipsum is simply dummy</div>
  <div class="quote-text">Lorem Ipsum is simply dummy text of the printing and typesetting industry. Lorem Ipsum has been the industry's standard dummy text ever.”</div>
  <div class="quote-name">Sam Rowe</div>
  <div class="quote-role">CEO Fawn Studio</div>
</div>

<div class="abs avatar" style="left:609px;top:2558px;width:86px;height:86px;background:linear-gradient(180deg,#f2b233,#c98a1f)" role="img" aria-label="Customer portrait"></div>
<div class="quote" style="left:716px">
  <div class="quote-title"><span>&#8220;</span>Lorem Ipsum is simply dummy</div>
  <div class="quote-text">Lorem Ipsum is simply dummy text of the printing and typesetting industry. Lorem Ipsum has been the industry's standard dummy text ever.”</div>
  <div class="quote-name">Sam Rowe</div>
  <div class="quote-role">CEO Fawn Studio</div>
</div>

<div class="abs" style="left:233px;top:2697px;width:732px;height:1px;background:var(--line)"></div>
<div class="abs center section-title" style="top:2744px">Subscribe Email</div>
<div class="abs center" style="top:2785px;font-size:10px;line-height:17px;color:#444">Subscribe now and receive weekly newsletter with Coaching materials, new courses, interest-<br>ing posts, popular books and much more!</div>
<div class="abs" style="left:433px;top:2848px;width:333px;height:29px;border-radius:15px;background:#fff;box-shadow:0 4px 14px rgba(0,0,0,.12)"></div>
<div class="abs" style="left:449px;top:2857px;font-size:8px;color:#555">Enter your email</div>
<div class="abs" style="left:698px;top:2848px;width:68px;height:29px;border-radius:0 15px 15px 0;background:var(--blue);color:#fff;font:500 7px/29px Roboto,sans-serif;text-align:center">SUBSCRIBE</div>

<div class="abs footer">
  <div class="abs" style="left:235px;top:42px;font:500 14px/18px Roboto,sans-serif;color:#fff;letter-spacing:.5px">GUARDLINE</div>
  <div class="abs" style="left:235px;top:70px;font-size:8px;line-height:19px">&#9742; &nbsp;+44 20 0000 1234<br>&#9993; &nbsp;info@guardline.example<br>&#9679; &nbsp;Lorem Ipsum, &nbsp;is simply dummy</div>
  <span class="social" style="left:234px"></span>
  <span class="social" style="left:265px;background:var(--blue);border-color:var(--blue)"></span>
  <span class="social" style="left:296px"></span>
  <span class="social" style="left:327px"></span>
  <div class="fcol" style="left:452px"><h5>CATEGORIES</h5><ul><li>Lorem Ipsum is</li><li>Lorem Ipsum is simply</li><li>Lorem Ipsum is</li><li>Lorem Ipsum is simply</li></ul></div>
  <div class="fcol" style="left:627px"><h5>CATEGORIES</h5><ul><li>Lorem Ipsum is</li><li>Lorem Ipsum is simply</li><li>Lorem Ipsum is</li><li>Lorem Ipsum is simply</li></ul></div>
  <div class="fcol" style="left:814px"><h5>CATEGORIES</h5><ul><li>Lorem Ipsum is</li><li>Lorem Ipsum is</li><li>simply</li><li>Lorem Ipsum is</li></ul></div>
</div>
<div class="abs footer-bottom">
  <span class="abs" style="left:235px;top:12px">© 2017 Guardline. All rights reserved.</span>
  <span class="abs" style="left:799px;top:12px">Privacy &nbsp;| &nbsp;Terms &nbsp;| &nbsp;Sitemap &nbsp;| &nbsp;Help</span>
</div>

</body>
</html>
```